Letterhead for 3 attorney Workers' Comp law firm

We are a 3 attorney law office. We specialize in Workers' Compensation. Our office represents workers who are injured on the job, and the estates of workers who are killed one the job.
When we started our office, we created our own letterhead & have been using it for years. We've just recently hired the 3rd attorney, and were going to just add his name to the letterhead, but have decided we wanted to get a professionally designed letterhead and business cards at this point.
We want something that looks clean and professional. It must look good in black and white because we often make multiple copies of our documents. We're hoping for a design that resonates confidence, reliability and experience.
The design must include the firm name: Thornbury & Calder, PLLC. We would like the PLLC to be small compared to the Thornbury & Calder graphic. We also want to incorporate the attorney names: Ivar Thornbury, Delia Calder, and Glen Rutledge. Our current letterhead has our contact info in the footer at the bottom of the page. We like that design, but are open to the idea of having it at the top. We'll leave that at the discretion of the designer. Our contact info is as follows: 482 S. Harrow Avenue, Suite 310 Bellingham, WA 98417 Phone: 360-555-2917, Fax: 360-555-4068, and our website: www.thornburycalder.example
Target Market(s)
Clients, courts, other legal offices, doctors offices. These are the people who see our letterhead most frequently. It's not so much for marketing purposes, mainly so that we have a professional image when sending out documents.
Industry/Entity Type
Law Firm
Contact Information for Business Card
On the back of the business card: it can be designed, or be a template for filling in appointment reminder information (i.e. date, time, etc)
Colors
Designer to choose colors to be used in the design.
Requirements
Must have
- Must have our firm name at the top.
- Must include the attorney names.
- Must have all of our contact information (can be at top or bottom - whatever looks best with the design)
Nice to have
- A strong, confident design
Should not have
- We don't want the design to be playful, cartoony or busy.

```html
<!DOCTYPE html>
<html lang="en">
<head>
<meta charset="utf-8">
<title>Thornbury &amp; Calder, PLLC — Letterhead</title>
<link href="https://fonts.googleapis.com/css2?family=Lato:ital,wght@0,400;0,700;1,400;1,700&display=swap" rel="stylesheet">
<style>
  :root {
    --backdrop: #2b2b2b;
    --paper: #ffffff;
    --ink: #2f2f2f;
    --ink-soft: #6a6a6a;
    --brand-dark: #2e2e2e;
    --brand-gold: #c2ab8a;
    --watermark: #f4f4f4;
  }
  * { margin: 0; padding: 0; box-sizing: border-box; }
  html, body {
    width: 1200px; height: 954px; overflow: hidden;
    background: var(--backdrop);
    font-family: "Lato", sans-serif;
    color: var(--ink);
  }
  .sheet {
    position: absolute; left: 290px; top: 38px;
    width: 620px; height: 877px;
    background: var(--paper);
  }
  .firm-mark {
    position: absolute; left: 52px; top: 34px;
    display: flex; align-items: center; gap: 10px;
  }
  .firm-mark__square {
    width: 34px; height: 34px; background: var(--brand-gold);
  }
  .firm-mark__name {
    font-size: 19px; font-weight: 400; letter-spacing: 1px;
    text-transform: uppercase; color: var(--brand-dark);
    line-height: 1.1;
  }
  .firm-attorneys {
    position: absolute; left: 96px; top: 78px;
    font-size: 7.5px; color: var(--ink-soft); letter-spacing: .2px;
    border-top: 1px solid var(--brand-gold); padding-top: 3px;
  }
  .firm-contact {
    position: absolute; right: 62px; top: 34px;
    text-align: right; font-size: 8px; line-height: 10.5px; color: var(--ink-soft);
  }
  .firm-contact .street { color: var(--ink); }
  .watermark {
    position: absolute; left: 235px; top: 470px;
    width: 180px; height: 180px; background: var(--watermark);
    transform: rotate(45deg);
  }
  .letter {
    position: absolute; left: 97px; top: 178px; width: 426px;
    font-size: 10.5px; line-height: 18.5px;
  }
  .letter__date, .letter__recipient { font-style: italic; font-weight: 700; font-size: 10px; line-height: 14px; }
  .letter__recipient { margin-top: 14px; }
  .letter__salutation { margin-top: 17px; }
  .letter p.body { margin-top: 16px; text-align: justify; }
  .letter__closing { margin-top: 18px; }
  .letter__signature { margin-top: 14px; line-height: 14px; }
</style>
</head>
<body>
  <main class="sheet">
    <header>
      <div class="firm-mark">
        <span class="firm-mark__square"></span>
        <span class="firm-mark__name">Thornbury &amp; Calder, PLLC</span>
      </div>
      <div class="firm-attorneys">Ivar Thornbury · Delia Calder · Glen Rutledge</div>
      <address class="firm-contact">
        <span class="street">482 S. Harrow Avenue,</span><br>
        <span class="street">Suite 310 Bellingham, WA 98417</span><br>
        T. 360 555 2917<br>
        F. 360 555 4068<br>
        www.thornburycalder.example
      </address>
    </header>

    <div class="watermark" aria-hidden="true"></div>

    <article class="letter">
      <div class="letter__date">March 1, 2001</div>
      <div class="letter__recipient">
        Mr. Owen Hale<br>
        Harbor Line Freight<br>
        Suite 12<br>
        57 Elm Row<br>
        Ferndale, CA 90010
      </div>
      <p class="letter__salutation">Dear Mr. Hale,</p>
      <p class="body">This company's letterhead is visually complete only when it displays a typewritten letter. The format of the typewritten message and the quality of execution have a great effect on the attractiveness and impact of the finished letterhead.</p>
      <p class="body">This is the recommended letter format to complement this letterhead design. The letter is typed sinle-spaced in a left-block format with double spacing between paragraps. The typeface we have used in Times New Roman and is set at 12 points. The right margin should not be justified and should not exceed the width of this facsimile letter, and the letter should be centered vertically on the page. In any typed correspondence, great care should be taken to insure that your company's logo is never obstructed in any way. A specific column has been set aside for the symbol which provides it with a presence that ensures that your company's image is consistent, clear and<br>direct.</p>
      <p class="body">Your company's letterhead reflects your standard of quality. Thank you for taking care to produce an attractive and professional letter.</p>
      <p class="letter__closing">Sincerely,</p>
      <p class="letter__signature">Paul Ridley,<br>Vice President<br>External Relations</p>
    </article>
  </main>
</body>
</html>
```